BUSINESS CARD FOR GUITAR SCHOOL

I would like to design a business card for my Guitar Music School. The school is called "Pluck & Meadow".

The card should be yellow.

Target Market(s)

18-35 years old

Industry/Entity Type

School

Contact Information for Business Card

I would like to design a business card for my Guitar Music School. The school is called "Pluck & Meadow". The card should be yellow.

Card must be consistent with my website design: www.pluckandmeadow.com.sg

Requirements
Must have
• 1) Name of Company
• 2) Company Logo
• 3) Name of Employee
• 4) Position of Employee
• 5) Contact Number
• 6) Address
Nice to have
• Creative Design
• Card must be consistent with my website design: www.pluckandmeadow.com.sg
Should not have
• Boring Design

```html
<!DOCTYPE html>
<html lang="en">
<head>
<meta charset="utf-8">
<title>Pluck &amp; Meadow — Business Card</title>
<link rel="stylesheet" href="https://fonts.googleapis.com/css2?family=Arimo:wght@400;700&display=swap">
<style>
  :root {
    --canvas: #ffffff;
    --card-yellow: #f3c92f;
    --card-yellow-soft: #f7dc79;
    --card-pale: #fdf6da;
    --deco-yellow: #f6d556;
    --ink: #3b3a36;
    --ink-dark: #111111;
  }
  * { box-sizing: border-box; margin: 0; padding: 0; }
  html, body {
    width: 1200px;
    height: 350px;
    overflow: hidden;
    background: var(--canvas);
  }
  .sheet {
    position: relative;
    width: 1200px;
    height: 350px;
  }
  .card {
    position: absolute;
    top: 0;
    height: 350px;
    overflow: hidden;
  }
  .card--front {
    left: 0;
    width: 614px;
    background: var(--card-yellow);
  }
  .card--back {
    left: 626px;
    width: 574px;
    background: linear-gradient(90deg, var(--card-yellow) 0%, var(--card-yellow) 45%, var(--card-yellow-soft) 75%, var(--card-pale) 100%);
  }
  .deco-art {
    position: absolute;
    border-radius: 40px;
  }
  .card--front .deco-art {
    left: 170px;
    top: 10px;
    width: 320px;
    height: 310px;
    background: radial-gradient(ellipse at center, var(--deco-yellow) 0%, rgba(246, 213, 86, 0) 70%);
  }
  .card--back .deco-art {
    left: 330px;
    top: 60px;
    width: 240px;
    height: 280px;
    background: radial-gradient(ellipse at center, rgba(255, 255, 255, 0.35) 0%, rgba(255, 255, 255, 0) 70%);
  }
  .brand {
    position: absolute;
    left: 40px;
    top: 84px;
    display: flex;
    align-items: flex-start;
    gap: 22px;
    font-family: "Arimo", Arial, sans-serif;
    font-weight: 700;
    color: var(--ink);
  }
  .brand__name {
    font-size: 78px;
    line-height: 0.9;
    letter-spacing: -3px;
  }
  .brand__mark {
    width: 30px;
    height: 30px;
    margin-top: 22px;
    border-radius: 50%;
    background: var(--ink);
    flex: none;
  }
  .brand__tagline {
    position: absolute;
    left: 190px;
    top: 232px;
    font-family: "Arimo", Arial, sans-serif;
    font-size: 17px;
    color: var(--ink);
    letter-spacing: 0.1px;
    white-space: nowrap;
  }
  .contact-item {
    position: absolute;
    left: 92px;
    display: flex;
    align-items: center;
    gap: 36px;
  }
  .contact-item--name { top: 68px; }
  .contact-item--address { top: 156px; }
  .contact-item--phone { top: 240px; }
  .contact-item__icon {
    width: 54px;
    height: 46px;
    flex: none;
  }
  .contact-item__text {
    font-family: "Arimo", Arial, sans-serif;
    font-size: 27px;
    line-height: 1.02;
    color: var(--ink-dark);
    white-space: nowrap;
  }
</style>
</head>
<body>
  <main class="sheet">
    <section class="card card--front">
      <div class="deco-art" role="img" aria-label="Faint guitar headstock and leaf decoration"></div>
      <div class="brand">
        <span class="brand__name">Pluck &amp;<br>Meadow</span>
        <span class="brand__mark"></span>
      </div>
      <p class="brand__tagline">Playing From the Heart Each Day</p>
    </section>

    <section class="card card--back">
      <div class="deco-art" role="img" aria-label="Faint guitar headstock decoration"></div>
      <div class="contact-item contact-item--name">
        <svg class="contact-item__icon" viewBox="0 0 54 46" aria-hidden="true">
          <polygon points="0,2 34,8 12,30" fill="#111"/>
          <polygon points="7,9 41,15 19,37" fill="#111" stroke="#f3c92f" stroke-width="2"/>
          <polygon points="14,16 50,18 30,44" fill="#111" stroke="#f3c92f" stroke-width="2"/>
        </svg>
        <span class="contact-item__text">Harlan Surname<br>Position</span>
      </div>
      <div class="contact-item contact-item--address">
        <svg class="contact-item__icon" viewBox="0 0 54 46" aria-hidden="true">
          <polygon points="0,2 34,8 12,30" fill="#111"/>
          <polygon points="7,9 41,15 19,37" fill="#111" stroke="#f3c92f" stroke-width="2"/>
          <polygon points="14,16 50,18 30,44" fill="#111" stroke="#f3c92f" stroke-width="2"/>
        </svg>
        <span class="contact-item__text">Address Details</span>
      </div>
      <div class="contact-item contact-item--phone">
        <svg class="contact-item__icon" viewBox="0 0 54 46" aria-hidden="true">
          <polygon points="0,2 34,8 12,30" fill="#111"/>
          <polygon points="7,9 41,15 19,37" fill="#111" stroke="#f3c92f" stroke-width="2"/>
          <polygon points="14,16 50,18 30,44" fill="#111" stroke="#f3c92f" stroke-width="2"/>
        </svg>
        <span class="contact-item__text">Phone Number</span>
      </div>
    </section>
  </main>
</body>
</html>
```